Design a Pre-Workout Package Design For a Supplement Company!

Create a colourful and energetic design for our pre-workout packaging! A small container that holds 30 servings of pre-workout needs to be designed to be eye-catching and inspirational! We want it to jump off the shelf into your face and scream positivity, energy and colour.

I've attached our logo- ZYVRA Performance which should be the face of the package with the colourful packaging behind it! Feel free to change it around! I've also attached a supplement company's pre-workout design that I love! Good luck!!!

Target Market(s)

Fitness goers

Industry/Entity Type

Fitness

Colors

Designer to choose colors to be used in the design.

Requirements
Must have
• -Logo-ZYVRA Performance on the front
• - Colourful, energetic, inspiration package

```html
<!DOCTYPE html>
<html lang="en">
<head>
<meta charset="utf-8">
<title>ZYVRA Performance Pre-Workout Label</title>
<link rel="stylesheet" href="https://fonts.googleapis.com/css2?family=Montserrat:wght@400;500;600;700;800&display=swap">
<style>
  :root {
    --stage: #d4d4d4;
    --white: #ffffff;
    --lime: #9be21c;
    --badge: #3a1f8f;
    --band: rgba(22, 14, 92, 0.78);
    --pink: #f23ce0;
    --pink-deep: #e42fd6;
    --blue: #1a16e6;
    --blue-deep: #1410c8;
    --navy: #241089;
    --navy-deep: #1d0c78;
  }
  * { box-sizing: border-box; margin: 0; padding: 0; }
  html, body {
    width: 1200px; height: 1200px; overflow: hidden;
    background: var(--stage);
    font-family: "Montserrat", sans-serif;
    color: var(--white);
  }
  .label {
    position: absolute; left: 50px; top: 122px;
    width: 1100px; height: 956px; overflow: hidden;
  }
  .label-art {
    position: absolute; inset: 0;
    background:
      radial-gradient(ellipse 22% 30% at 8% 25%, rgba(190,240,40,0.85), transparent 70%),
      radial-gradient(ellipse 18% 28% at 35% 18%, rgba(240,250,255,0.7), transparent 70%),
      radial-gradient(ellipse 20% 26% at 60% 10%, rgba(255,90,200,0.75), transparent 70%),
      radial-gradient(ellipse 16% 24% at 88% 8%, rgba(255,40,60,0.85), transparent 70%),
      radial-gradient(ellipse 22% 30% at 75% 40%, rgba(120,230,255,0.6), transparent 70%),
      radial-gradient(ellipse 18% 20% at 95% 35%, rgba(250,240,120,0.6), transparent 70%),
      radial-gradient(ellipse 25% 20% at 20% 85%, rgba(80,40,220,0.8), transparent 70%),
      radial-gradient(ellipse 22% 14% at 75% 96%, rgba(170,240,60,0.7), transparent 70%),
      linear-gradient(160deg, #2a3bf0 0%, #1a20d8 45%, #2c14b8 75%, #3b22d0 100%);
  }
  .servings-badge {
    position: absolute; left: 153px; top: 71px;
    width: 192px; height: 192px; border-radius: 50%;
    background: var(--badge);
    display: flex; flex-direction: column; align-items: center; justify-content: center;
    color: var(--lime);
  }
  .servings-count { font-size: 84px; font-weight: 700; line-height: 0.9; letter-spacing: -3px; }
  .servings-unit { font-size: 23px; font-weight: 500; margin-top: 4px; }
  .title-band {
    position: absolute; left: 0; top: 403px; width: 100%; height: 139px;
    background: var(--band);
  }
  .brand {
    position: absolute; left: 40px; top: 412px; width: 420px;
    font-weight: 800; color: var(--white); text-align: center;
  }
  .brand-name { font-size: 108px; line-height: 1; letter-spacing: -3px; }
  .brand-sub { font-size: 27px; line-height: 1; letter-spacing: 1px; margin-top: 34px; }
  .product { position: absolute; left: 513px; top: 426px; }
  .product-name { font-size: 66px; font-weight: 600; line-height: 1; letter-spacing: -1px; }
  .product-type { font-size: 25px; font-weight: 500; letter-spacing: 3px; margin-top: 10px; }
  .claims { position: absolute; left: 513px; top: 550px; width: 587px; list-style: none; }
  .claim { display: flex; align-items: center; height: 98px; margin-bottom: 13px; }
  .claim-value {
    width: 106px; height: 100%;
    display: flex; align-items: center; justify-content: center;
    font-size: 54px; font-weight: 500;
  }
  .claim-text {
    flex: 1; height: 100%; display: flex; align-items: center;
    padding-left: 20px; font-size: 26px; font-weight: 600; letter-spacing: 2px;
  }
  .claim-value { border-radius: 8px 0 0 8px; }
  .claim--caffeine .claim-value { background: var(--pink); }
  .claim--caffeine .claim-text { background: var(--pink-deep); }
  .claim--banned .claim-value { background: var(--blue); }
  .claim--banned .claim-text { background: var(--blue-deep); }
  .claim--ingredients .claim-value { background: var(--navy); }
  .claim--ingredients .claim-text { background: var(--navy-deep); }
  .net-weight { position: absolute; left: 148px; top: 768px; }
  .net-weight-label { font-size: 24px; font-weight: 400; }
  .net-weight-value { font-size: 34px; font-weight: 500; letter-spacing: 1px; margin-top: 8px; }
</style>
</head>
<body>
  <main class="label">
    <div class="label-art" role="img" aria-label="Abstract fluid paint artwork in electric blue, violet, lime, pink, red and white swirls"></div>

    <div class="servings-badge">
      <span class="servings-count">30</span>
      <span class="servings-unit">servings</span>
    </div>

    <div class="title-band"></div>

    <div class="brand">
      <div class="brand-name">ZYVRA</div>
      <div class="brand-sub">PERFORMANCE</div>
    </div>

    <div class="product">
      <h1 class="product-name">PRE-WORKOUT</h1>
      <p class="product-type">DIETARY SUPPLEMENT</p>
    </div>

    <ul class="claims">
      <li class="claim claim--caffeine"><span class="claim-value">0</span><span class="claim-text">CAFFEINE FREE</span></li>
      <li class="claim claim--banned"><span class="claim-value">0</span><span class="claim-text">BANNED SUBSTANCES</span></li>
      <li class="claim claim--ingredients"><span class="claim-value">10</span><span class="claim-text">ACTIVE INGREDIENTS</span></li>
    </ul>

    <div class="net-weight">
      <p class="net-weight-label">NET WEIGHT:</p>
      <p class="net-weight-value">594 LBS &nbsp;(270g)</p>
    </div>
  </main>
</body>
</html>
```